Business card design for holistic health care clinic

We need a double-sided business card design for our holistic health care clinic that integrates our logo design and also its color scheme. My business is called Veluma. It is an integrative medicine clinic. You have already done the logo for me. Please ensure an elegant and upscale design that is not cluttered, but still has all the necessary information (please see below for details).

Target Market(s)

Wellness, fitness, rehabilitation for educated, well-traveled open-minded clients who are focused on natural, organic, balanced and preventive healthcare and lifestyle.

Industry/Entity Type

Medical

Contact Information for Business Card

Modern, clean.

Number of Pages Required

1 page

Font styles to use
Serif
Sans Serif

Colors

Designer to choose colors to be used in the design.

Requirements
Must have
• Logo on one side, all other information on the other side.
• Other information should include:
• Tomas Brevik - DOE, CPT, LMT
• 4120 North Harlow Street
• Austin, TX 78631
• 512 608 2947
• 818 459 7208
• info@VelumaHealth.com
• t.brevik@VelumaHealth.com
Nice to have
• Darker background on front - but not totally black - shaded/dark gray.

```html
<!DOCTYPE html>
<html lang="en">
<head>
<meta charset="utf-8">
<title>Veluma Business Card</title>
<link rel="stylesheet" href="https://fonts.googleapis.com/css2?family=Nunito:wght@800&family=Roboto:wght@400&family=Roboto+Condensed:wght@700&display=swap">
<style>
  :root {
    --backdrop: #5a4838;
    --card-light: #f3f3f3;
    --card-dark: #2a2a2a;
    --card-dark-top: #1f1f1f;
    --brand-blue: #0a8bc6;
    --text-gray: #4a4a4a;
    --rule-gray: #8c8c8c;
    --band-gray: #a4a4a4;
    --white: #ffffff;
  }
  * { margin: 0; padding: 0; box-sizing: border-box; }
  html, body { width: 1200px; height: 960px; overflow: hidden; }
  body { background: var(--backdrop); position: relative; font-family: "Roboto", Arial, sans-serif; }

  .card { position: absolute; width: 600px; height: 342px; border-radius: 20px; overflow: hidden; }
  .card-info { left: 314px; top: 114px; background: var(--card-light); }
  .card-brand { left: 311px; top: 472px; background: linear-gradient(180deg, var(--card-dark-top), var(--card-dark)); }

  .brand-name {
    position: absolute; font-family: "Nunito", Arial, sans-serif; font-weight: 800;
    color: var(--brand-blue); letter-spacing: 1px; line-height: 1;
  }
  .card-info .brand-name { right: 34px; top: 74px; font-size: 56px; }
  .card-brand .brand-name { left: 0; right: 0; top: 146px; text-align: center; font-size: 66px; }

  .holder { position: absolute; left: 34px; top: 177px; color: var(--brand-blue);
    font-family: "Roboto Condensed", Arial, sans-serif; font-weight: 700; }
  .holder-name { font-size: 21px; text-transform: uppercase; }
  .holder-credentials { font-size: 12.5px; }

  .divider { position: absolute; left: 35px; top: 212px; width: 530px; height: 1px; background: var(--rule-gray); }

  .contact-list { position: absolute; left: 35px; top: 226px; list-style: none; }
  .contact-list li { display: flex; align-items: center; height: 19.5px; font-size: 14.5px; color: var(--text-gray); }
  .contact-list svg { width: 13px; height: 13px; margin-right: 9px; fill: var(--brand-blue); }

  .address { position: absolute; right: 35px; top: 246px; text-align: right; font-size: 14.5px;
    line-height: 19px; color: var(--text-gray); font-style: normal; }

  .footer-bands { position: absolute; left: 0; bottom: 0; width: 600px; height: 40px; }
  .website { position: absolute; right: 30px; bottom: 11px; color: var(--white); font-size: 14.5px; letter-spacing: 1.2px; }

  .tagline { position: absolute; left: 0; right: 0; top: 282px; text-align: center; color: var(--white); font-size: 15px; }
</style>
</head>
<body>

<section class="card card-info">
  <div class="brand-name">VELUMA</div>

  <div class="holder">
    <span class="holder-name">Tomas Brevik</span>
    <span class="holder-credentials">- DOE, CPT, LMT</span>
  </div>
  <div class="divider"></div>

  <ul class="contact-list">
    <li>
      <svg viewBox="0 0 24 24"><path d="M6.6 10.8a15.1 15.1 0 0 0 6.6 6.6l2.2-2.2a1 1 0 0 1 1-.25 11.4 11.4 0 0 0 3.6.57 1 1 0 0 1 1 1V20a1 1 0 0 1-1 1A17 17 0 0 1 3 4a1 1 0 0 1 1-1h3.5a1 1 0 0 1 1 1c0 1.25.2 2.45.57 3.57a1 1 0 0 1-.25 1z"/></svg>
      512 608 2947
    </li>
    <li>
      <svg viewBox="0 0 24 24"><path d="M7 1h10a2 2 0 0 1 2 2v18a2 2 0 0 1-2 2H7a2 2 0 0 1-2-2V3a2 2 0 0 1 2-2zm0 3v14h10V4zm5 15.5a1 1 0 1 0 0 2 1 1 0 0 0 0-2z"/></svg>
      818 459 7208
    </li>
    <li>
      <svg viewBox="0 0 24 24"><path d="M2 5h20v2l-10 6L2 7zm0 4 10 6 10-6v10H2z"/></svg>
      t.brevik@VelumaHealth.com
    </li>
  </ul>

  <address class="address">4120 North Harlow Street<br>Austin, TX 78631</address>

  <svg class="footer-bands" viewBox="0 0 600 40" preserveAspectRatio="none">
    <rect x="0" y="22" width="600" height="18" fill="var(--band-gray)"/>
    <polygon points="340,2 600,2 600,40 318,40" fill="var(--card-light)"/>
    <polygon points="344,2 600,2 600,40 322,40" fill="var(--brand-blue)"/>
  </svg>
  <div class="website">www.VelumaHealth.com</div>
</section>

<section class="card card-brand">
  <div class="brand-name">VELUMA</div>
  <p class="tagline">it’s all about you – your health, your objectives</p>
</section>

</body>
</html>
```